BriskwayLane.com needs updated website design.

BriskwayLane.com offers individuals a quick, hassle-free way of selling their car, rv, or boat in the Sun City Center, FL area. We will come to the customer's place of choosing in order to give them an in-person offer for their car, rv, or boat. Looking for a website design that will allow users to input their vehicle details as well as their contact info in order to schedule a time and place for our staff to come make them an offer. Currently have an active site that can be referenced.

Target Market(s)

Older people who no longer need their cars.

Industry/Entity Type

Automotive

Coding

Coded - Design and coding required

Number of Pages Required

3 page

Font styles to use
Sans Serif

Colors
a1cd3a
33b8a4

Requirements
Must have
• Trustworthy theme, Emphasis on capturing contact info (contact form visible at all times). Standard privacy policy. Wordpress theme

```html
<!DOCTYPE html>
<html lang="en">
<head>
<meta charset="utf-8">
<title>BriskwayLane.com – Sell Your Car Today</title>
<link href="https://fonts.googleapis.com/css2?family=Poppins:ital,wght@0,400;0,500;0,600;0,700;1,600&display=swap" rel="stylesheet">
<style>
:root{
  --lime:#a1cd3a;
  --teal:#33b8a4;
  --ink:#1c1c1c;
  --text:#555;
  --muted:#777;
  --soft:#f7f7f7;
  --navy:#06121c;
  --line:#e6e6e6;
  --white:#fff;
}
*{box-sizing:border-box;margin:0;padding:0}
html,body{width:1200px;height:3001px;overflow:hidden}
body{font-family:'Poppins',sans-serif;color:var(--ink);background:var(--white);position:relative}
.wrap{width:750px;margin:0 auto;position:relative}
section,header,footer{position:relative;width:1200px}
.btn{display:inline-flex;align-items:center;gap:10px;background:var(--teal);color:var(--white);font-weight:600;font-size:14px;border-radius:20px;padding:4px 22px 4px 4px;height:32px;white-space:nowrap;line-height:1}
.btn .dot{width:26px;height:26px;border-radius:50%;background:var(--white);display:inline-block;border:3px solid var(--lime);flex:none}
.sec-title{text-align:center;font-size:20px;font-weight:700}

/* top bar */
.topbar{height:37px;background:var(--lime);color:var(--white);font-size:10px;font-weight:600}
.topbar .wrap{display:flex;align-items:center;height:37px;gap:18px}
.topbar .social{margin-left:auto;display:flex;gap:6px}
.topbar .social span{width:19px;height:19px;background:#1d2b10;border-radius:2px;display:block}

/* header */
.site-header{height:75px;border-bottom:1px solid var(--line)}
.site-header .wrap{display:flex;align-items:center;height:75px}
.brand{display:flex;align-items:center;gap:8px}
.brand .mark{width:40px;height:40px;border-radius:50%;background:var(--teal);flex:none}
.brand .name{font-size:21px;font-weight:700;line-height:1}
.brand small{display:block;font-size:9px;color:var(--lime);font-weight:600;margin-top:3px}
.nav{margin-left:auto;display:flex;gap:31px;font-size:11px;align-items:center}

/* hero */
.hero{height:482px;background:linear-gradient(90deg,#1f6f66 0%,#2c8178 45%,#4c8e8f 75%,#7a9fa8 100%)}
.hero .wrap{height:482px}
.hero-copy{position:absolute;left:0;top:155px;width:390px;color:var(--white)}
.hero-copy h1{font-size:32px;line-height:1.18;font-weight:700}
.hero-copy .tag{font-style:italic;font-weight:600;font-size:14px;margin:18px 0 10px}
.hero-copy p{font-size:11.5px;line-height:1.65}
.quote-form{position:absolute;right:0;top:53px;width:322px;height:374px;background:var(--white);padding:20px 19px}
.quote-form h2{text-align:center;font-size:19px;font-weight:600;margin-bottom:20px}
.row{display:flex;gap:10px;margin-bottom:10px}
.field{flex:1;height:31px;background:#f1f2f2;font-size:9px;color:#666;display:flex;align-items:center;padding:0 9px;justify-content:space-between}
.field.full{margin-bottom:11px}
.quote-form .btn{margin:4px auto 0;display:flex;width:max-content}

/* features */
.features{height:224px}
.features .wrap{display:flex;justify-content:space-between;padding-top:48px;width:790px}
.feature{width:175px;text-align:center}
.feature .icon{width:60px;height:60px;margin:0 auto 26px;background:var(--white);box-shadow:0 0 8px rgba(0,0,0,.12);display:flex;align-items:center;justify-content:center}
.feature h3{color:var(--teal);font-size:14px;font-weight:600}
.feature p{font-size:11px;color:var(--text);margin-top:4px;white-space:nowrap}

/* sold cars */
.sold{height:518px;background:var(--soft)}
.sold .sec-title{padding-top:50px}
.cars{display:flex;gap:19px;position:absolute;left:62px;top:108px}
.car{width:200px;text-align:center}
.car .photo{height:187px;position:relative}
.car .badge{position:absolute;right:6px;bottom:6px;width:44px;height:44px;background:var(--white)}
.car h3{font-size:14px;font-weight:600;margin:14px 0 10px}
.car p{font-size:9.5px;color:var(--muted);line-height:1.45;padding:0 10px}
.car .price{font-size:11px;margin-top:16px}
.sold .cta{position:absolute;left:535px;top:438px}

/* about */
.about{height:343px;display:flex}
.about .photo{width:584px;height:343px;background:linear-gradient(120deg,#dfe3e6 0%,#b9c1c6 40%,#7f8c74 65%,#c9cfc3 100%)}
.about .panel{flex:1;background:var(--navy);color:var(--white);padding:58px 44px 0}
.about .panel > *{max-width:370px}
.about h2{font-size:19px;font-weight:700;margin-bottom:18px}
.about .lead{font-size:10.5px;font-weight:500;line-height:1.78;margin-bottom:22px}
.about ul{list-style:none}
.about li{font-size:10px;font-style:italic;line-height:1.75;padding-left:12px;position:relative;margin-bottom:9px}
.about li::before{content:"";position:absolute;left:0;top:7px;width:5px;height:5px;border-radius:50%;background:var(--lime)}

/* testimonials */
.testimonials{height:307px}
.testimonials .sec-title{padding-top:52px}
.reviews{display:flex;gap:50px;margin-top:30px}
.review{width:350px}
.review .who{display:flex;align-items:center;gap:12px}
.avatar{width:44px;height:44px;border-radius:50%;background:#c8cdd2}
.review h3{font-size:14px;font-weight:600}
.stars{color:var(--teal);font-size:11px;letter-spacing:1px}
.stars i{color:#ccc;font-style:normal}
.review p{font-size:10.5px;color:var(--text);line-height:1.78;margin-top:15px}

/* faq */
.faq{height:429px;background:var(--soft)}
.faq .sec-title{padding-top:52px;margin-bottom:28px}
.qa{background:var(--white);border:1px dashed #ddd;margin-bottom:10px}
.qa .q{height:40px;display:flex;align-items:center;justify-content:space-between;padding:0 12px;font-size:11.5px;font-weight:600}
.qa .q span{font-weight:400;font-size:16px;color:#555}
.qa .a{font-size:9px;color:var(--muted);line-height:2.05;padding:0 12px 10px}

/* brands */
.brands{height:236px}
.brands .sec-title{padding-top:50px}
.brand-row{display:flex;justify-content:space-between;align-items:center;margin-top:38px}
.brand-row span{font-size:12px;font-weight:600;color:#444;width:74px;text-align:center}

/* footer */
.site-footer{height:350px;background:#f5f5f5}
.footer-cols{display:flex;padding-top:48px}
.footer-about{width:300px}
.footer-about .brand .mark{width:30px;height:30px}
.footer-about .brand .name{font-size:14px}
.footer-about .brand small{font-size:7px}
.footer-about p{font-size:9.5px;color:var(--text);line-height:2;margin-top:17px}
.f-social{display:flex;gap:20px;margin-top:22px;align-items:center}
.f-social span{width:14px;height:14px;border-radius:50%;border:2px solid #333;display:block}
.f-social span.on{width:30px;height:30px;background:var(--teal);border:none}
.fcol h4{font-size:12.5px;font-weight:600;margin:12px 0 16px}
.fcol a{display:block;font-size:9px;color:var(--muted);text-decoration:none;margin-bottom:20px}
.fcol a.active{color:var(--teal)}
.fcol b{display:block;font-size:9px;font-weight:600;margin-bottom:3px}
.fcol .v{font-size:9px;color:var(--muted);line-height:1.9;margin-bottom:10px}
.copyright{position:absolute;left:0;right:0;bottom:13px;text-align:center;font-size:9px;color:var(--muted)}
</style>
</head>
<body>

<div class="topbar">
  <div class="wrap">
    <span>Call Us : 941-555-0187</span><span>|</span><span>Email : info@briskwaylane.com</span>
    <div class="social"><span></span><span></span><span></span><span></span></div>
  </div>
</div>

<header class="site-header">
  <div class="wrap">
    <div class="brand"><span class="mark"></span><div><div class="name">BriskwayLane.com</div><small>Sell your Car Today</small></div></div>
    <nav class="nav">
      <span>HOME</span><span>ABOUT US</span><span>CONTACT US</span>
      <span class="btn"><span class="dot"></span>Contact Us</span>
    </nav>
  </div>
</header>

<section class="hero" role="img" aria-label="Close-up of a car wheel and parked vehicles under a teal tint">
  <div class="wrap">
    <div class="hero-copy">
      <h1>Get Your Free In Person Cash Offer Today</h1>
      <div class="tag">"Don't Sell Til You Give Me A Yell"</div>
      <p>Lorem ipsum dolor sit amet, consectetur adipiscing elit, sed do eiusmod tempor incididunt ut labore et dolore magna aliqua. Ut enim ad minim veniam,</p>
    </div>
    <form class="quote-form">
      <h2>Get your Car Price</h2>
      <div class="row"><div class="field">Select Year <span>⌄</span></div><div class="field">Select Brand <span>⌄</span></div></div>
      <div class="row"><div class="field">Select Model <span>⌄</span></div><div class="field">Select Variant <span>⌄</span></div></div>
      <div class="row"><div class="field">Select City <span>⌄</span></div><div class="field">Kilometers Driven</div></div>
      <div class="field full">Full Name</div>
      <div class="field full">Email Address</div>
      <div class="field full">Mobile Number</div>
      <span class="btn"><span class="dot"></span>Submit Now</span>
    </form>
  </div>
</section>

<section class="features">
  <svg width="1200" height="60" style="position:absolute;left:0;top:40px" aria-hidden="true"><path d="M345 40 Q420 20 475 30 T650 45 T880 40" fill="none" stroke="#ccc" stroke-dasharray="3 3"/></svg>
  <div class="wrap">
    <div class="feature"><div class="icon"><svg width="36" height="36" viewBox="0 0 36 36" fill="none" stroke="#222" stroke-width="1.5"><circle cx="19" cy="20" r="12"/><circle cx="19" cy="20" r="8" stroke="var(--teal)"/><path d="M19 8V4M16 4h6M19 20l4-4"/></svg></div><h3>FAST</h3><p>I'll Be at Your Door Today</p></div>
    <div class="feature"><div class="icon"><svg width="36" height="36" viewBox="0 0 36 36" fill="none" stroke="#222" stroke-width="1.5"><path d="M18 4v22M8 8h20M8 8l-4 10h8zM28 8l-4 10h8z" stroke="var(--teal)"/><path d="M6 26q12 10 24 0"/></svg></div><h3>FAIR</h3><p>Get Fair Price for Your Vehicle</p></div>
    <div class="feature"><div class="icon"><svg width="36" height="36" viewBox="0 0 36 36" fill="none" stroke="#222" stroke-width="1.5"><path d="M10 30l8-10 8 10M14 6h8v10h-8z"/><path d="M4 22l8 8M32 22l-8 8" stroke="var(--teal)"/></svg></div><h3>FRIENDLY</h3><p>Trusted for Over 25 Years</p></div>
    <div class="feature"><div class="icon"><svg width="36" height="36" viewBox="0 0 36 36" fill="none" stroke="#222" stroke-width="1.5"><path d="M12 32V14l6-8 4 4-4 6h8v16z"/><path d="M24 6l4 4" stroke="var(--teal)"/></svg></div><h3>HASSLE FREE</h3><p>I Handle All the Paperwork</p></div>
  </div>
</section>

<section class="sold">
  <h2 class="sec-title">Recent Sold Cars</h2>
  <div class="cars">
    <div class="car"><div class="photo" role="img" aria-label="Yellow sports coupe parked on a leafy street" style="background:linear-gradient(160deg,#7a9a4e,#d8b91e 60%,#6d6d6d)"><span class="badge"></span></div><h3>Sunburst Coupe</h3><p>Lorem ipsum dolor sit amet consectetur adipiscing elit, sed do eiusmod tempor.</p><div class="price">Price:&nbsp; US$10,000.00</div></div>
    <div class="car"><div class="photo" role="img" aria-label="Yellow compact car in front of a stone building" style="background:linear-gradient(160deg,#b5a58a,#d9c25a 60%,#8b8577)"><span class="badge"></span></div><h3>Compact Family Car</h3><p>Lorem ipsum dolor sit amet consectetur adipiscing elit, sed do eiusmod tempor.</p><div class="price">Price:&nbsp; US$10,000.00</div></div>
    <div class="car"><div class="photo" role="img" aria-label="White off-road vehicle on a forest trail" style="background:linear-gradient(160deg,#3d4a33,#d6d8d4 55%,#5a5a4a)"><span class="badge"></span></div><h3>Adventure Trail 4x4</h3><p>Lorem ipsum dolor sit amet consectetur adipiscing elit, sed do eiusmod tempor.</p><div class="price">Price:&nbsp; US$10,000.00</div></div>
    <div class="car"><div class="photo" role="img" aria-label="Red classic convertible near pine trees" style="background:linear-gradient(160deg,#3f5a44,#9a2a1c 55%,#8a8a88)"><span class="badge"></span></div><h3>Sunburst Coupe</h3><p>Lorem ipsum dolor sit amet consectetur adipiscing elit, sed do eiusmod tempor.</p><div class="price">Price:&nbsp; US$10,000.00</div></div>
    <div class="car"><div class="photo" role="img" aria-label="White SUV parked by wooden pallets" style="background:linear-gradient(160deg,#7a6a5a,#e8e8e8 55%,#9a9a9a)"><span class="badge"></span></div><h3>Sunburst Coupe</h3><p>Lorem ipsum dolor sit amet consectetur adipiscing elit, sed do eiusmod tempor.</p><div class="price">Price:&nbsp; US$10,000.00</div></div>
  </div>
  <span class="btn cta"><span class="dot"></span>Sell My Car</span>
</section>

<section class="about">
  <div class="photo" role="img" aria-label="Hand passing car keys beside a fan of cash in front of a white car"></div>
  <div class="panel">
    <h2>About Us</h2>
    <p class="lead">We offer the most convenient way of selling your vehicle. We will come to you at a place of your choosing, i.e. home, office, or any other public place.&nbsp; We will give you an in person cash offer on the spot.</p>
    <ul>
      <li>Got an old clunker? I'll But it! – Turn it into cash today!</li>
      <li>Got a nice car you just don't need? I'll Buy it! – Stop wasting money on insurance, registration and maintenance costs!</li>
      <li>Got a car that needs repairs? I'll Buy It! – No matter what the issue is I'll come take it away today!</li>
    </ul>
  </div>
</section>

<section class="testimonials">
  <h2 class="sec-title">Customer Testimonial</h2>
  <div class="wrap reviews">
    <div class="review"><div class="who"><span class="avatar" role="img" aria-label="Customer portrait"></span><div><h3>Harold Mercer</h3><div class="stars">★★★★<i>★</i></div></div></div><p>Lorem ipsum dolor sit amet, consectetur adipiscing elit, sed do eiusmod tempor incididunt ut labore et dolore magna aliqua. Ut enim ad minim veniam, quis nostrud exercitation ullamco laboris nisi ut aliquip ex ea commodo consequat. Duis aute irure dolor in reprehenderit in voluptate velit esse cillum dolore eu fugiat.</p></div>
    <div class="review"><div class="who"><span class="avatar" role="img" aria-label="Customer portrait"></span><div><h3>Dorothy Ashford</h3><div class="stars">★★★★<i>★</i></div></div></div><p>Lorem ipsum dolor sit amet, consectetur adipiscing elit, sed do eiusmod tempor incididunt ut labore et dolore magna aliqua. Ut enim ad minim veniam, quis nostrud exercitation ullamco laboris nisi ut aliquip ex ea commodo consequat. Duis aute irure dolor in reprehenderit in voluptate velit esse cillum dolore eu fugiat.</p></div>
  </div>
</section>

<section class="faq">
  <h2 class="sec-title">Frequently Asked Questions</h2>
  <div class="wrap">
    <div class="qa"><div class="q">Who is Briskway Lane?<span>–</span></div><div class="a">Lorem ipsum dolor sit amet, consectetur adipiscing elit, sed do eiusmod tempor incididunt ut labore et dolore magna aliqua. Ut enim ad minim veniam, quis nostrud exercitation ullamco laboris nisi ut aliquip ex ea commodo consequat. Duis aute irure dolor in reprehenderit in voluptate velit esse cillum dolore eu fugiat. Lorem ipsum dolor sit amet, consectetur adipiscing elit, sed do eiusmod tempor incididunt ut labore et dolore magna aliqua. Ut enim ad minim veniam, quis nostrud exercitation ullamco laboris nisi ut aliquip ex ea commodo consequat. Duis aute irure dolor in reprehenderit in voluptate velit esse cillum dolore eu fugiat.</div></div>
    <div class="qa"><div class="q">Eiusmod tempor incididunt ut labore et dolore?<span>+</span></div></div>
    <div class="qa"><div class="q">Exercitation Ullamco Laboris Nisi Ut Aliquip?<span>+</span></div></div>
    <div class="qa"><div class="q">Lorem Ipsum Dolor Sit Amet?<span>+</span></div></div>
  </div>
</section>

<section class="brands">
  <h2 class="sec-title">Top Car Brands</h2>
  <div class="wrap brand-row">
    <span>Vantor</span><span>Kessel</span><span>Lynwood</span><span>Crestline</span><span>Hanamo</span><span>Ridgeback</span><span>Velocci</span><span>Quadra</span><span>Sternhaus</span>
  </div>
</section>

<footer class="site-footer">
  <div class="wrap footer-cols">
    <div class="footer-about">
      <div class="brand"><span class="mark"></span><div><div class="name">BriskwayLane.com</div><small>Sell your Car Today</small></div></div>
      <p>Lorem ipsum dolor sit amet, adipiscing elit. Quod corrupti laborum, quasi? Dolor sapiente amet optio harum dolores, voluptate, tempora dolorem fugiat fuga autem. Lorem ipsum dolor sit amet, adipiscing elit. Quod corrupti laborum.</p>
      <div class="f-social"><span class="on"></span><span></span><span></span><span></span><span></span></div>
    </div>
    <div class="fcol" style="width:156px">
      <h4>Useful Links</h4><a href="#">About Us</a><a href="#" class="active">- Services</a><a href="#">Blog</a><a href="#">FAQs</a><a href="#">Contact Us</a>
    </div>
    <div class="fcol" style="width:139px">
      <h4>Other Links</h4><a href="#">Support</a><a href="#">Privacy Policy</a><a href="#">Terms &amp; Conditions</a><a href="#">Sitemap</a>
    </div>
    <div class="fcol" style="width:155px">
      <h4>Contact Us</h4>
      <b>Address:-</b><div class="v">418 Palm Crest Avenue, Sun City Center, FL 33573, USA.</div>
      <b>Mobile:-</b><div class="v">941-555-0187</div>
      <b>Email Address:-</b><div class="v">info@briskwaylane.com</div>
    </div>
  </div>
  <div class="copyright">Copyright © 2020 Briskway Lane. All Rights Reserved</div>
</footer>

</body>
</html>
```